Brightwater Health Partners, LLC Business Card update!

would like a classier business card. Our cards currently just have our logo and contact information. Need better use of color and creativity
Logo attached.

Target Market(s)

Potential clients, contacts, existing clients. We are a consulting company

Industry/Entity Type

Business

Contact Information for Business Card

We like our colors but just have a boring card with our logo and a white background. I want something that stands out.

Colors
ec1f27
757575

Requirements
Must have
• Color to stay consistent. Logo provided
Nice to have
• Just better use of color/ design

```html
<!DOCTYPE html>
<html lang="en">
<head>
<meta charset="utf-8">
<title>Brightwater Health Partners – Business Card</title>
<link rel="stylesheet" href="https://fonts.googleapis.com/css2?family=Lato:wght@400;700&display=swap">
<style>
  :root {
    --brand-red: #ec1f27;
    --brand-red-light: #f4525a;
    --brand-grey: #757575;
    --stripe-grey: #a9a9a9;
    --card-white: #ffffff;
    --card-white-shade: #ececec;
    --page-bg: #e7e4df;
    --text-on-red: #ffffff;
  }
  * { margin: 0; padding: 0; box-sizing: border-box; }
  html, body {
    width: 1200px;
    height: 1023px;
    overflow: hidden;
    background: var(--page-bg);
    font-family: "Lato", Arial, sans-serif;
  }
  .stage {
    width: 1200px;
    height: 1023px;
    display: flex;
    align-items: center;
    justify-content: center;
  }
  .business-card {
    position: relative;
    width: 900px;
    height: 514px;
    border-radius: 26px;
    overflow: hidden;
    background: linear-gradient(135deg, var(--card-white) 40%, var(--card-white-shade));
    box-shadow: 0 14px 34px rgba(0,0,0,0.18);
  }
  .card-shapes {
    position: absolute;
    inset: 0;
  }
  .brand-lockup {
    position: absolute;
    left: 44px;
    top: 196px;
    display: flex;
    align-items: center;
    gap: 16px;
  }
  .brand-dot {
    width: 54px;
    height: 54px;
    border-radius: 50%;
    background: var(--brand-grey);
    flex: none;
  }
  .brand-name {
    color: var(--brand-red);
    font-weight: 400;
    line-height: 1;
  }
  .brand-name .line-main {
    display: block;
    font-size: 34px;
    letter-spacing: 0.5px;
  }
  .brand-name .line-sub {
    display: block;
    font-size: 22px;
    margin-top: 4px;
  }
  .address-block {
    position: absolute;
    left: 400px;
    top: 362px;
    color: var(--text-on-red);
    font-size: 20px;
    font-weight: 700;
    font-style: normal;
    line-height: 1.35;
  }
  .contact-divider {
    position: absolute;
    left: 636px;
    top: 330px;
    width: 2px;
    height: 100px;
    background: rgba(255,255,255,0.55);
  }
  .contact-list {
    position: absolute;
    left: 596px;
    top: 118px;
    list-style: none;
    color: var(--text-on-red);
    font-size: 19px;
    line-height: 1;
  }
  .contact-list li {
    display: flex;
    align-items: center;
    gap: 12px;
    margin-bottom: 14px;
  }
  .contact-icon {
    width: 17px;
    height: 17px;
    flex: none;
    fill: var(--text-on-red);
  }
</style>
</head>
<body>
<main class="stage">
  <article class="business-card">
    <svg class="card-shapes" width="900" height="514" viewBox="0 0 900 514" aria-hidden="true">
      <defs>
        <linearGradient id="redPanel" x1="0" y1="1" x2="1" y2="0">
          <stop offset="0" stop-color="#f4525a"/>
          <stop offset="0.55" stop-color="#ec1f27"/>
          <stop offset="1" stop-color="#e0141c"/>
        </linearGradient>
      </defs>
      <path class="grey-swoosh" d="M568 0 C440 150 318 330 300 514 L336 514 C352 330 476 150 604 0 Z" fill="#a9a9a9"/>
      <path class="red-panel" d="M604 0 C476 150 352 330 336 514 L900 514 L900 0 Z" fill="url(#redPanel)"/>
    </svg>

    <div class="brand-lockup">
      <span class="brand-dot"></span>
      <p class="brand-name">
        <span class="line-main">BRIGHTWATER</span>
        <span class="line-sub">Health Partners</span>
      </p>
    </div>

    <address class="address-block">
      1480 Larkspur Lane<br>
      Fairview, WI 50000-00
    </address>

    <span class="contact-divider"></span>

    <ul class="contact-list">
      <li>
        <svg class="contact-icon" viewBox="0 0 18 18"><path d="M4 1h3l1.5 4-2 1.5a10 10 0 0 0 5 5L13 9.5l4 1.5v3a2 2 0 0 1-2 2A14 14 0 0 1 2 3a2 2 0 0 1 2-2z"/></svg>
        555-014-2870
      </li>
      <li>
        <svg class="contact-icon" viewBox="0 0 18 18"><path d="M4 1h10v5H4z M1 7h16v8h-3v2H4v-2H1z M6 12v3h6v-3z"/></svg>
        555-014-2871
      </li>
      <li>
        <svg class="contact-icon" viewBox="0 0 18 18"><path d="M1 3h16v12H1z M2.5 4.5 9 10l6.5-5.5z" fill-rule="evenodd"/></svg>
        hello@brightwaterhp.com
      </li>
      <li>
        <svg class="contact-icon" viewBox="0 0 18 18"><path d="M1 2h16v12H10v2h3v1H5v-1h3v-2H1z M3 4v8h12V4z" fill-rule="evenodd"/></svg>
        www.brightwaterhp.com
      </li>
    </ul>
  </article>
</main>
</body>
</html>
```